Shopify store for hemp

I need a store designed for Shopify for my hemp company. I currently have a brick and mortar store, but we are looking to get some business online as well. I will upload our logo for reference. We want a clean look. Categories like THCA Flower, Concentrates, Vapes, Edibles would be nice so that we can put individual products under them. I want something about all products being third-party lab tested. All products are sourced in the United States.
Updates

Target Market(s)

Former customers who live in different areas and signed up for our marketing list.

Industry/Entity Type

Hemp/Cannabis

Coding

Coded - Design and coding required

Number of Pages Required

1 page

Requirements
Must have
• Clean feel

```html
<!DOCTYPE html>
<html lang="en">
<head>
<meta charset="utf-8">
<title>Ridgeline Hemp — Premium Hemp Products</title>
<link href="https://fonts.googleapis.com/css2?family=Outfit:wght@500;600;700&family=Nunito+Sans:wght@400;600;700&display=swap" rel="stylesheet">
<style>
:root{
  --green:#16a34a;
  --green-dark:#15803d;
  --mint:#e8f8ec;
  --mint-soft:#f1fbf3;
  --ink:#0f172a;
  --text:#334155;
  --muted:#64748b;
  --line:#e5e7eb;
  --panel:#f8fafc;
  --blue:#2563eb;
  --purple:#9333ea;
  --footer:#141b2d;
  --white:#ffffff;
}
*{box-sizing:border-box;margin:0;padding:0}
html,body{width:1200px;height:3841px;overflow:hidden;background:var(--white)}
body{position:relative;font-family:"Nunito Sans",sans-serif;color:var(--text)}
.abs{position:absolute}
h1,h2,h3{font-family:"Outfit",sans-serif;color:var(--ink)}
.btn{position:absolute;display:flex;align-items:center;justify-content:center;border-radius:999px;font-weight:700;font-size:15px;text-decoration:none}
.btn-green{background:var(--green);color:var(--white)}
.btn-outline{border:2px solid var(--green);color:var(--green);background:var(--white)}

/* hero */
.hero-bg{left:0;top:0;width:1200px;height:640px;background:linear-gradient(180deg,#fff 0%,var(--mint) 18%,var(--mint-soft) 100%);clip-path:polygon(0 0,100% 0,100% 84%,0 99%)}
.nav{left:31px;top:16px;width:1138px;height:75px;background:var(--white);border-radius:38px;box-shadow:0 6px 18px rgba(15,23,42,.08)}
.brand{left:28px;top:18px;display:flex;align-items:center;gap:10px;font-family:"Outfit",sans-serif;font-weight:600;font-size:17px;color:var(--ink)}
.brand-mark{width:40px;height:40px;border-radius:50%;background:#8fb9a0}
.nav-links{left:350px;top:11px;width:366px;height:52px;border-radius:26px;background:#f1f5f4;display:flex;align-items:center;justify-content:space-evenly;font-size:15px;color:var(--ink)}
.nav .btn{left:992px;top:15px;width:116px;height:44px}
.hero-title{left:30px;top:222px;font-size:47px;line-height:46px;font-weight:700}
.hero-title span{color:var(--green)}
.hero-copy{left:30px;top:335px;width:490px;font-size:17.5px;line-height:26px;color:var(--text)}
.hero-media{left:622px;top:181px;width:548px;height:360px;border-radius:10px;background:linear-gradient(135deg,#0b0714 0%,#2a0f3f 45%,#3a1a6e 70%,#12081f 100%)}
.badge-cert{left:1059px;top:508px;width:124px;height:47px;border-radius:8px;background:var(--white);box-shadow:0 4px 14px rgba(15,23,42,.12);display:flex;align-items:center;gap:8px;padding-left:16px;font-size:13px;color:var(--ink)}
.dot{width:10px;height:10px;border-radius:50%;background:var(--green)}

/* features */
.feature{top:691px;width:360px;height:184px;border-radius:10px;background:var(--panel);text-align:center;padding-top:24px}
.feature .icon{width:44px;height:44px;border-radius:50%;margin:0 auto 14px;display:flex;align-items:center;justify-content:center}
.feature h3{font-family:"Nunito Sans",sans-serif;font-weight:600;font-size:17px;margin-bottom:10px}
.feature p{font-size:14px;line-height:23px;color:var(--muted);padding:0 28px}

/* categories */
.cat-bg{left:0;top:934px;width:1200px;height:790px;background:linear-gradient(180deg,var(--panel) 0%,var(--panel) 70%,#fff 100%)}
.section-title{left:0;width:1200px;text-align:center;font-size:35px;font-weight:600}
.section-lead{left:250px;width:700px;text-align:center;font-size:17px;line-height:26px;color:var(--text)}
.card{top:1175px;width:262px;height:416px;border-radius:10px;background:var(--white);box-shadow:0 6px 18px rgba(15,23,42,.08);overflow:hidden}
.card-media{height:210px;position:relative}
.tag{position:absolute;right:14px;top:16px;background:var(--green);color:var(--white);font-size:12px;font-weight:600;padding:3px 10px;border-radius:999px}
.card h3{font-family:"Nunito Sans",sans-serif;font-weight:600;font-size:18px;margin:26px 22px 10px}
.card p{font-size:14px;line-height:23px;color:var(--muted);margin:0 22px}
.card .btn{left:22px;width:218px;height:44px;font-size:14px}

/* lab */
.lab-media{left:30px;top:1902px;width:547px;height:359px;border-radius:8px;background:linear-gradient(135deg,#d9dde0 0%,#f3f1ee 45%,#c9ccd0 75%,#6b7280 100%);box-shadow:0 8px 22px rgba(15,23,42,.15)}
.lab-title{left:622px;top:1860px;font-size:35px;font-weight:600}
.lab-copy{left:622px;top:1922px;width:548px;font-size:17px;line-height:27px}
.check{position:absolute;left:622px;display:flex;gap:14px}
.check .tick{width:20px;height:20px;border-radius:50%;background:#dcfce7;display:flex;align-items:center;justify-content:center;margin-top:2px}
.check b{display:block;font-size:15px;color:var(--ink);font-weight:600}
.check span{font-size:14px;color:var(--muted)}
.btn-blue{left:622px;top:2250px;width:178px;height:51px;background:var(--blue);color:var(--white)}

/* about */
.about-bg{left:0;top:2497px;width:1200px;height:628px;background:linear-gradient(180deg,var(--mint) 0%,var(--mint-soft) 100%);clip-path:polygon(0 0,100% 0,100% 87%,0 100%)}
.value{top:2770px;width:380px;text-align:center}
.value .icon{width:60px;height:60px;border-radius:50%;margin:0 auto 22px;display:flex;align-items:center;justify-content:center}
.value h3{font-family:"Nunito Sans",sans-serif;font-weight:600;font-size:18px;margin-bottom:12px}
.value p{font-size:14px;line-height:22px;color:var(--muted);padding:0 20px}

/* newsletter */
.email{left:389px;top:3333px;width:295px;height:45px;border:1px solid var(--line);border-radius:999px;padding-left:16px;display:flex;align-items:center;font-size:14px;color:#9ca3af}

/* footer */
.footer{left:0;top:3453px;width:1200px;height:388px;background:var(--footer);color:#cbd5e1}
.footer .brand{left:30px;top:62px;color:var(--white)}
.footer-about{left:30px;top:114px;width:430px;font-size:14px;line-height:23px;color:#e2e8f0}
.social{left:30px;top:172px;display:flex;gap:16px}
.social i{display:block;width:20px;height:20px;border-radius:50%;background:#9aa5b8}
.footer-col{top:70px}
.footer-col h4{font-family:"Nunito Sans",sans-serif;font-weight:700;font-size:15px;color:var(--white);margin-bottom:14px}
.footer-col li{list-style:none;font-size:14px;line-height:30px;color:#e2e8f0}
.footer-rule{left:30px;top:278px;width:1140px;height:1px;background:#273248}
.copyright{left:0;top:308px;width:1200px;text-align:center;font-size:13px;color:#9aa5b8}
</style>
</head>
<body>

<div class="abs hero-bg"></div>
<header class="abs nav">
  <div class="abs brand"><span class="brand-mark"></span>Ridgeline Hemp</div>
  <nav class="abs nav-links"><span>Products</span><span>About</span><span>Lab Testing</span><span>Contact</span></nav>
  <a class="btn btn-green">Shop Now</a>
</header>

<h1 class="abs hero-title">Premium Hemp Products<br><span>Lab Tested &amp; Pure</span></h1>
<p class="abs hero-copy">Discover our carefully curated selection of premium hemp products. All items are third-party lab tested and sourced exclusively in the United States.</p>
<a class="btn btn-green" style="left:30px;top:444px;width:187px;height:58px">Browse Products</a>
<a class="btn btn-outline" style="left:233px;top:444px;width:148px;height:58px">Learn More</a>
<div class="abs hero-media" role="img" aria-label="Featured hemp product photo"></div>
<div class="abs badge-cert"><span class="dot"></span>Lab Certified</div>

<div class="abs feature" style="left:30px">
  <div class="icon" style="background:#dcfce7"><svg width="20" height="20" viewBox="0 0 20 20" fill="none" stroke="#16a34a" stroke-width="1.8"><circle cx="10" cy="10" r="7.5"/><path d="M6.5 10.2l2.4 2.3 4.6-4.8"/></svg></div>
  <h3>Third-Party Lab Tested</h3>
  <p>Every product undergoes rigorous testing for purity and potency</p>
</div>
<div class="abs feature" style="left:419px">
  <div class="icon" style="background:#dbeafe"><svg width="20" height="20" viewBox="0 0 20 20" fill="none" stroke="#2563eb" stroke-width="1.8"><path d="M5 17V3h9l-2 3.5 2 3.5H5"/></svg></div>
  <h3>US Sourced</h3>
  <p>All products sourced exclusively from trusted US farms</p>
</div>
<div class="abs feature" style="left:809px">
  <div class="icon" style="background:#f3e8ff"><svg width="20" height="20" viewBox="0 0 20 20" fill="none" stroke="#9333ea" stroke-width="1.8"><rect x="4.5" y="9" width="11" height="8" rx="1.5"/><path d="M7 9V6.5a3 3 0 016 0V9"/></svg></div>
  <h3>Premium Quality</h3>
  <p>Carefully curated selection of the finest hemp products</p>
</div>

<div class="abs cat-bg"></div>
<h2 class="abs section-title" style="top:1008px">Product Categories</h2>
<p class="abs section-lead" style="top:1064px;left:260px;width:680px">Explore our comprehensive selection of premium hemp products, each category carefully curated for quality and effectiveness.</p>

<article class="abs card" style="left:30px">
  <div class="card-media" role="img" aria-label="THCA flower product photo" style="background:linear-gradient(135deg,#0b0714 0%,#2a0f3f 50%,#3a1a6e 80%,#12081f 100%)"><span class="tag">Lab Tested</span></div>
  <h3>THCA Flower</h3>
  <p>Premium indoor and outdoor flower strains with verified potency and purity.</p>
  <a class="btn btn-green" style="top:349px">Shop Flower</a>
</article>
<article class="abs card" style="left:322px">
  <div class="card-media" role="img" aria-label="Concentrates product photo" style="background:linear-gradient(135deg,#f7a865 0%,#f5985a 60%,#f3b07e 100%)"><span class="tag">Lab Tested</span></div>
  <h3>Concentrates</h3>
  <p>High-quality extracts including wax, shatter, and live resin products.</p>
  <a class="btn btn-green" style="top:349px">Shop Concentrates</a>
</article>
<article class="abs card" style="left:614px">
  <div class="card-media" role="img" aria-label="Vape cartridges product photo" style="background:#f3f4f6"><span class="tag">Lab Tested</span></div>
  <h3>Vapes</h3>
  <p>Premium vape cartridges and disposables with pure, clean extracts.</p>
  <a class="btn btn-green" style="top:349px">Shop Vapes</a>
</article>
<article class="abs card" style="left:908px">
  <div class="card-media" role="img" aria-label="Edibles lifestyle photo" style="background:linear-gradient(180deg,#e8ece9 0%,#cfd6d2 60%,#7a6f66 100%)"><span class="tag">Lab Tested</span></div>
  <h3>Edibles</h3>
  <p>Delicious gummies, chocolates, and treats with precise dosing.</p>
  <a class="btn btn-green" style="top:327px">Shop Edibles</a>
</article>

<div class="abs lab-media" role="img" aria-label="Lab technician working at a microscope"></div>
<h2 class="abs lab-title">Third-Party Lab Testing</h2>
<p class="abs lab-copy">Every product in our store undergoes rigorous third-party laboratory testing to ensure the highest standards of quality, purity, and potency. We believe in complete transparency and provide detailed lab reports for all our products.</p>
<div class="check" style="top:2056px"><div class="tick"><svg width="12" height="12" viewBox="0 0 12 12" fill="none" stroke="#16a34a" stroke-width="2"><path d="M2.5 6.2l2.2 2.1 4.8-4.8"/></svg></div><div><b>Potency Testing</b><span>Accurate cannabinoid profiles and concentration levels</span></div></div>
<div class="check" style="top:2116px"><div class="tick"><svg width="12" height="12" viewBox="0 0 12 12" fill="none" stroke="#16a34a" stroke-width="2"><path d="M2.5 6.2l2.2 2.1 4.8-4.8"/></svg></div><div><b>Purity Analysis</b><span>Screening for pesticides, heavy metals, and contaminants</span></div></div>
<div class="check" style="top:2176px"><div class="tick"><svg width="12" height="12" viewBox="0 0 12 12" fill="none" stroke="#16a34a" stroke-width="2"><path d="M2.5 6.2l2.2 2.1 4.8-4.8"/></svg></div><div><b>Microbial Testing</b><span>Ensuring products are free from harmful bacteria and mold</span></div></div>
<a class="btn btn-blue">View Lab Reports</a>

<div class="abs about-bg"></div>
<h2 class="abs section-title" style="top:2570px">About Our Company</h2>
<p class="abs section-lead" style="top:2632px;left:180px;width:840px">From our brick-and-mortar roots to serving customers nationwide, we're committed to providing the highest quality hemp products. Our journey began with a simple mission: to offer pure, lab-tested hemp products that you can trust.</p>
<div class="abs value" style="left:20px">
  <div class="icon" style="background:var(--green)"><svg width="24" height="24" viewBox="0 0 24 24" fill="none" stroke="#fff" stroke-width="1.8"><rect x="6" y="4" width="12" height="16"/><path d="M9 8h2M13 8h2M9 12h2M13 12h2M11 20v-3h2v3"/></svg></div>
  <h3>Established Store</h3>
  <p>Years of experience serving customers in our physical location</p>
</div>
<div class="abs value" style="left:410px">
  <div class="icon" style="background:var(--blue)"><svg width="24" height="24" viewBox="0 0 24 24" fill="none" stroke="#fff" stroke-width="1.8"><circle cx="12" cy="12" r="8"/><path d="M4 12h16M12 4c3 3 3 13 0 16M12 4c-3 3-3 13 0 16"/></svg></div>
  <h3>US Sourced</h3>
  <p>All products sourced exclusively from trusted American farms</p>
</div>
<div class="abs value" style="left:801px">
  <div class="icon" style="background:var(--purple)"><svg width="24" height="24" viewBox="0 0 24 24" fill="none" stroke="#fff" stroke-width="1.8"><path d="M12 19s-7-4.3-7-9.2A3.8 3.8 0 0112 7.6a3.8 3.8 0 017 2.2C19 14.7 12 19 12 19z"/></svg></div>
  <h3>Customer First</h3>
  <p>Dedicated to providing exceptional service and quality products</p>
</div>

<h2 class="abs section-title" style="top:3196px">Stay Updated</h2>
<p class="abs section-lead" style="top:3254px;left:225px;width:750px">Join our mailing list to receive updates on new products, special offers, and hemp industry news.</p>
<div class="abs email">Enter your email</div>
<a class="btn btn-green" style="left:699px;top:3333px;width:111px;height:45px">Subscribe</a>

<footer class="abs footer">
  <div class="abs brand"><span class="brand-mark" style="width:36px;height:36px"></span>Ridgeline Hemp</div>
  <p class="abs footer-about">Premium hemp products sourced in the USA and third-party lab tested for your peace of mind. From our store to your door.</p>
  <div class="abs social" aria-label="Social links"><i></i><i></i><i></i></div>
  <div class="abs footer-col" style="left:614px"><h4>Quick Links</h4><ul><li>THCA Flower</li><li>Concentrates</li><li>Vapes</li><li>Edibles</li><li>Lab Reports</li></ul></div>
  <div class="abs footer-col" style="left:908px"><h4>Support</h4><ul><li>Contact Us</li><li>Shipping Info</li><li>Returns</li><li>FAQ</li><li>Privacy Policy</li></ul></div>
  <div class="abs footer-rule"></div>
  <p class="abs copyright">© 2024 Ridgeline Hemp. All rights reserved. | Third-party lab tested | US sourced products</p>
</footer>

</body>
</html>
```